Home Based Business Website Design

Need 1 template web design. Require clean friendly website design that helps promote a work from home business opportunity based around personal development. The site should lean towards appealing to the female market (see target market) and be straight forward, fresh colours and good use of white space. The site should have a family focus using imagery of happy families and reinforcing the quality of life and freedom available. The site should be in a two or three column format, navigation can be top or left, there will be 6 menu items in total (E.g. home, about, testimonials, contact, faq, why me?). There should be space for a video, text, images and a clear "call to action" (contact us). The site should come across as professiona, positive, friendly and trustworthy. Scope for many more sites of this nature in the future.

Target Market(s)

People that are ready for change. People wanting to make money from a business at home. 25+ years old, mum's , professional. People that are tired of the commute and want a better quality of life. While the site should lean towards focusing on stay at home mums or working mums looking for a better life it should also be able to appeal to a wider audience (male and female) so should not be too "girly"!

Industry/Entity Type

Business

Requirements
Must have
• Fairly open to interpretation, site must have at least two columns, clear call to action, space for a video, text and images, navigation (single level 6 items).
Nice to have
• Possibly animated banner of images?
Should not have
• Try to use less obvious imagery no stressed out executives or people jumping for joy. no dark designs no purple or flouro colours. Site should be modern in design.

```html
<!DOCTYPE html>
<html lang="en">
<head>
<meta charset="utf-8">
<title>yourcompanyname – Home</title>
<link rel="stylesheet" href="https://fonts.googleapis.com/css2?family=Arimo:wght@400;700&family=Oswald:wght@400&display=swap">
<style>
  :root {
    --ink: #000000;
    --paper: #ffffff;
    --brand-blue: #1e95c4;
    --brand-blue-deep: #0b6fa6;
    --bubble-light: #bfe3f5;
    --bubble-mid: #7cc4e8;
    --nav-text: #d9d9d9;
    --footer-text: #ffffff;
  }
  * { margin: 0; padding: 0; box-sizing: border-box; }
  html, body { width: 1200px; height: 900px; overflow: hidden; background: var(--paper); }
  .page { position: relative; width: 1200px; height: 900px; overflow: hidden; font-family: "Arimo", Arial, sans-serif; }

  .site-header { position: absolute; left: 0; top: 0; width: 1200px; height: 210px; }
  .header-shape { position: absolute; left: 0; top: 0; }
  .main-nav { position: absolute; top: 24px; right: 14px; display: flex; align-items: center; }
  .main-nav a { color: var(--nav-text); text-decoration: none; font-size: 14px; font-weight: 700; letter-spacing: 4px; }
  .main-nav .divider { color: var(--nav-text); font-size: 13px; margin: 0 14px 0 10px; }
  .brand-name { position: absolute; left: 56px; top: 78px; font-family: "Oswald", "Arial Narrow", sans-serif; font-size: 72px; line-height: 1; color: var(--paper); letter-spacing: -1px; }

  .video-player { position: absolute; left: 64px; top: 260px; width: 445px; height: 361px; background: var(--ink); border-radius: 12px; }
  .play-button { position: absolute; left: 247px; top: 407px; }

  .cta-contact { position: absolute; left: 80px; top: 656px; width: 432px; height: 166px; text-decoration: none; }
  .cta-contact svg { position: absolute; left: 0; top: 0; }
  .cta-label { position: absolute; left: 0; top: 28px; width: 432px; padding-left: 10px; text-align: center; font-family: "Oswald", "Arial Narrow", sans-serif; font-size: 68px; line-height: 1; color: var(--paper); letter-spacing: -1px; }

  .gallery { position: absolute; left: 607px; top: 260px; display: grid; grid-template-columns: repeat(3, 166px); grid-template-rows: repeat(3, 166px); column-gap: 20px; row-gap: 25px; }
  .gallery-tile { width: 166px; height: 166px; }
  .tile-kitchen { background: linear-gradient(160deg, #e6e6e4, #c9c3b8 60%, #e2a54a); }
  .tile-desk { background: linear-gradient(180deg, #4b6b3a, #6b5a3f 55%, #3a2c20); }
  .tile-phone { background: linear-gradient(150deg, #e8dccb, #d8a3a8 55%, #8a6a52); }
  .tile-laptop { background: linear-gradient(160deg, #f1efe8, #c88c6a 55%, #e8e6e0); }
  .tile-sofa { background: linear-gradient(180deg, #e7e3cf, #c9bf7a 55%, #b58c3a); }
  .tile-money { background: radial-gradient(circle at 50% 45%, #c4a06a, #f2f0ea 70%); }
  .tile-keyboard { background: linear-gradient(150deg, #b9bbbd, #e6e7e8 60%, #9fa1a3); }
  .tile-planner { background: linear-gradient(160deg, #a8424a, #c92a2a 55%, #6a4a3a); }
  .tile-coffee { background: linear-gradient(160deg, #efe9df, #caa27a 50%, #e8e8e8); }

  .site-footer { position: absolute; left: 0; top: 867px; width: 1200px; height: 33px; background: var(--brand-blue); }
  .copyright { position: absolute; left: 50px; top: 10px; font-size: 12px; font-weight: 700; color: var(--footer-text); }
</style>
</head>
<body>
<div class="page">
  <header class="site-header">
    <svg class="header-shape" width="1200" height="210" viewBox="0 0 1200 210" aria-hidden="true">
      <path d="M0 0 H1200 V186 C900 176 400 178 0 204 Z" fill="var(--brand-blue)"/>
      <path d="M0 0 H1200 V160 C850 150 350 150 0 168 Z" fill="var(--ink)"/>
    </svg>
    <nav class="main-nav">
      <a href="#">HOME</a><span class="divider">I</span>
      <a href="#">ABOUT</a><span class="divider">I</span>
      <a href="#">TESTIMONIALS</a><span class="divider">I</span>
      <a href="#">CONTACT</a><span class="divider">I</span>
      <a href="#">FAQ</a><span class="divider">I</span>
      <a href="#">WHY ME?</a>
    </nav>
    <div class="brand-name">yourcompanyname</div>
  </header>

  <main>
    <div class="video-player" aria-label="Video player"></div>
    <svg class="play-button" width="70" height="70" viewBox="0 0 70 70" aria-hidden="true">
      <circle cx="35" cy="35" r="34" fill="#e9eef2"/>
      <circle cx="35" cy="35" r="27" fill="var(--brand-blue-deep)"/>
      <circle cx="35" cy="31" r="22" fill="#3fa6dc" opacity="0.6"/>
      <path d="M28 22 L49 35 L28 48 Z" fill="#0d2f55"/>
    </svg>

    <a class="cta-contact" href="#">
      <svg width="432" height="166" viewBox="0 0 432 166" aria-hidden="true">
        <defs>
          <linearGradient id="bubbleFill" x1="0" y1="0" x2="0" y2="1">
            <stop offset="0" stop-color="var(--bubble-light)"/>
            <stop offset="0.5" stop-color="var(--bubble-mid)"/>
            <stop offset="1" stop-color="var(--bubble-light)"/>
          </linearGradient>
        </defs>
        <ellipse cx="216" cy="160" rx="200" ry="5" fill="#000" opacity="0.06"/>
        <path d="M24 4 H406 Q428 4 428 26 V108 Q428 130 406 130 H372 V162 L300 130 H28 Q4 130 4 106 V26 Q4 4 24 4 Z" fill="var(--brand-blue-deep)"/>
        <path d="M28 12 H400 Q418 12 418 30 V104 Q418 120 400 120 H362 V146 L302 120 H32 Q14 120 14 102 V30 Q14 12 28 12 Z" fill="url(#bubbleFill)"/>
      </svg>
      <span class="cta-label">CONTACT US</span>
    </a>

    <section class="gallery">
      <div class="gallery-tile tile-kitchen" role="img" aria-label="Photo of a mother and child at a laptop in a bright kitchen"></div>
      <div class="gallery-tile tile-desk" role="img" aria-label="Photo of a laptop on a wooden desk by a garden window"></div>
      <div class="gallery-tile tile-phone" role="img" aria-label="Photo of a woman on the phone working at a laptop at home"></div>
      <div class="gallery-tile tile-laptop" role="img" aria-label="Photo of a smiling woman working on a laptop"></div>
      <div class="gallery-tile tile-sofa" role="img" aria-label="Photo of a woman relaxing on a sofa with a laptop"></div>
      <div class="gallery-tile tile-money" role="img" aria-label="Image of a dollar sign on a stack of bank notes"></div>
      <div class="gallery-tile tile-keyboard" role="img" aria-label="Close-up photo of a computer keyboard"></div>
      <div class="gallery-tile tile-planner" role="img" aria-label="Photo of a woman with a planner and calculator at home"></div>
      <div class="gallery-tile tile-coffee" role="img" aria-label="Photo of a coffee mug beside a notebook and keyboard"></div>
    </section>
  </main>

  <footer class="site-footer">
    <p class="copyright">2009. ALL RIGHTS RESERVED</p>
  </footer>
</div>
</body>
</html>
```